Every sort of trade everysortoftrade.ca

Website for company offering Every sort of trade
Welding/Fabrication/Metal repairs/Metal building, Electrical repairs and installations, Plumbing and Heating, Renovations, Flooring, Paiting, and other services

We need a very clean and professional website outlining the many services we have

We would like each type of service to have its own page, with images of those types of services on those pages.

Then in the future, we can update those pages with projects we have done of those types.

Every Sort of Trade . CA

Located in Calgary, Alberta, Canada, offering services Alberta wide

Welding/Fabrication/Repair/Building - Steel and metals
Electrical contractor - Journeyman , small or large projects
Plumbing and Heating
Renovations
Flooring
Painting
Other services - storage, trucking, delivery, etc

business and residential services

Contractor

Coded - Design and coding required

5+ page

Sans Serif

3176b5
0253a1
85acd3
85abd2
cedeed
ffffff

Must have
• Clean
• Professional
• Easy of updating text and images

```html
<!DOCTYPE html>
<html lang="en">
<head>
<meta charset="utf-8">
<title>Every Sort of Trade</title>
<link rel="stylesheet" href="https://fonts.googleapis.com/css2?family=Open+Sans:ital,wght@0,400;0,600;0,700;0,800;1,700&family=Noto+Serif:ital,wght@1,700&display=swap">
<style>
:root{
  --blue:#3176b5;
  --blue-deep:#0253a1;
  --blue-soft:#85acd3;
  --blue-pale:#cedeed;
  --white:#ffffff;
  --ink:#1d1d1d;
  --body:#6b6b6b;
  --band:#f6f6f6;
  --footer:#050505;
}
*{box-sizing:border-box;margin:0;padding:0}
html,body{width:1200px;height:3930px;overflow:hidden}
body{font-family:"Open Sans",Arial,sans-serif;color:var(--ink);background:var(--white);position:relative}

.site-header{position:absolute;top:0;left:0;width:1200px;height:73px;background:var(--blue-deep);z-index:2;display:flex;align-items:center;justify-content:space-between;padding:0 150px}
.brand{color:var(--white);font-weight:800;font-size:26px;letter-spacing:-.3px;text-transform:uppercase;white-space:nowrap}
.main-nav{display:flex;font-size:12px;color:var(--white);text-transform:uppercase;white-space:nowrap}
.main-nav a{color:var(--white);text-decoration:none}
.main-nav a.active{font-weight:700}
.main-nav .sep{margin:0 14px;opacity:.8}

.hero{position:absolute;top:0;left:0;width:1200px;height:550px}
.hero-photo{position:absolute;inset:0;background:linear-gradient(100deg,#3b6ea3 0%,#9fb4c8 30%,#e9edf0 55%,#d9c9b1 80%,#c9a77a 100%)}
.hero-quote{position:absolute;top:248px;width:100%;text-align:center;font-family:"Noto Serif",Georgia,serif;font-style:italic;font-weight:700;font-size:42px;color:var(--white);white-space:nowrap}
.quote-pill{position:absolute;top:327px;left:290px;width:620px;height:66px;background:var(--white);border-radius:33px;display:flex;align-items:center;justify-content:space-between;padding:0 10px 0 30px;white-space:nowrap}
.quote-question{font-weight:700;font-size:21px;color:#333}
.btn-quote{flex-shrink:0;background:var(--blue);color:var(--white);font-weight:700;font-size:20px;line-height:1;border-radius:24px;padding:14px 22px;text-transform:uppercase}

.about{position:absolute;top:550px;left:0;width:1200px;height:354px;background:var(--band);padding:50px 144px 0}
.section-title{font-weight:600;font-size:30px;text-transform:uppercase;color:var(--ink);white-space:nowrap}
.section-title em{font-style:normal;color:var(--blue)}
.about-cols{display:flex;gap:36px;margin-top:20px}
.about-cols p{flex:1;font-size:11.5px;line-height:1.55;color:var(--body)}

.btn{display:inline-block;background:var(--blue);color:var(--white);font-weight:700;font-size:13px;text-transform:uppercase;border-radius:23px;width:152px;height:46px;line-height:46px;text-align:center;white-space:nowrap}
.about .btn{margin-top:30px}

.features{position:absolute;top:904px;left:0;width:1200px;height:348px;display:flex;justify-content:center;padding-top:100px}
.feature{width:230px;text-align:center}
.feature svg{width:80px;height:80px;display:block;margin:0 auto}
.feature h3{font-weight:400;font-size:15px;margin-top:28px;text-transform:uppercase;white-space:nowrap}

.service{position:absolute;left:0;width:1200px;height:362px;display:flex}
.service.flip{flex-direction:row-reverse}
.service-photo{width:600px;height:362px}
.service-text{width:600px;height:362px;padding:78px 44px 0 68px;background:var(--white)}
.service.flip .service-text{background:var(--band);padding-left:73px;padding-right:70px}
.service-text h2{font-weight:600;font-size:28px;text-transform:uppercase;white-space:nowrap}
.service-text p{font-size:11.5px;line-height:1.6;color:var(--body);margin-top:22px;max-width:462px}
.service-text .btn{margin-top:26px}

.more{position:absolute;top:3424px;left:0;width:1200px;height:186px}
.more-line{position:absolute;left:599px;top:0;width:2px;height:70px;background:var(--blue)}
.btn-outline{position:absolute;top:70px;left:508px;width:184px;height:50px;line-height:46px;border:2px solid var(--blue);border-radius:25px;text-align:center;font-size:13px;text-transform:uppercase;color:#333;background:var(--white);white-space:nowrap}

.site-footer{position:absolute;top:3610px;left:0;width:1200px;height:320px;background:var(--footer);color:#cfcfcf}
.footer-title{font-size:13px;text-transform:uppercase;color:#e5e5e5}
.message{position:absolute;left:144px;top:47px}
.fields{display:flex;gap:15px;margin-top:24px}
.field{width:186px;height:30px;border:1px solid #d8d8d8;font-size:11px;color:#cfcfcf;padding:7px 10px}
.field.area{width:388px;height:63px;margin-top:12px}
.btn-subscribe{margin-top:24px;width:100px;height:34px;border:1px solid var(--blue-soft);font-size:11px;color:#e5e5e5;text-align:center;line-height:32px}
.contact{position:absolute;left:768px;top:47px;font-size:11px;line-height:1.75;color:#bdbdbd}
.contact .footer-title{margin-bottom:12px;text-transform:none;font-size:14px}
.follow{position:absolute;left:768px;top:188px}
.follow .footer-title{text-transform:none;font-size:14px}
.social{display:flex;gap:8px;margin-top:20px}
.social span{width:34px;height:34px;border:2px solid #e5e5e5;background:var(--footer)}
</style>
</head>
<body>

<header class="site-header">
  <div class="brand">Every Sort of Trade</div>
  <nav class="main-nav">
    <a class="active">Home</a><span class="sep">/</span>
    <a>About Us</a><span class="sep">/</span>
    <a>Services</a><span class="sep">/</span>
    <a>Gallery</a><span class="sep">/</span>
    <a>Contact Us</a>
  </nav>
</header>

<section class="hero">
  <div class="hero-photo" role="img" aria-label="Photo of a tradesman fixing plumbing under a kitchen sink while a client watches"></div>
  <p class="hero-quote">“We provide every sort of trade”</p>
  <div class="quote-pill"><span class="quote-question">Are you interested in an estimate?</span><span class="btn-quote">Get a quote</span></div>
</section>

<section class="about">
  <h1 class="section-title">About <em>Every Sort of Trade</em></h1>
  <div class="about-cols">
    <p>We believe in quality beginnings and flawless finishes. We are a team of skilled tradespeople and contractors with years of experience in welding, electrical, plumbing, heating and renovation work. Our careful planning process is matched by an unflinching commitment to quality workmanship. Our team takes on small repairs and large projects alike, for business and residential clients across Alberta.</p>
    <p>Calgary is a city that keeps building, and its homes and workplaces need trades they can trust. We fabricate and repair steel and metal structures, install wiring and fixtures, lay floors and finish walls. From storage and trucking to delivery, we bring the right people and tools to every job and stand behind the result.</p>
  </div>
  <a class="btn">Know more</a>
</section>

<section class="features">
  <div class="feature">
    <svg viewBox="0 0 80 80" fill="none" stroke="#3176b5" stroke-width="3" stroke-linecap="round"><circle cx="44" cy="44" r="25"/><path d="M44 44 L44 28 M44 44 L55 50 M38 12 H50 M44 12 V19 M8 36 H16 M4 46 H14 M8 56 H16"/></svg>
    <h3>On time</h3>
  </div>
  <div class="feature">
    <svg viewBox="0 0 80 80" fill="none" stroke="#3176b5" stroke-width="3" stroke-linejoin="round"><path d="M30 10 H50 L56 26 V70 H24 V26 Z"/><circle cx="40" cy="20" r="3"/><path d="M46 38 C44 34 34 34 34 40 C34 46 46 44 46 51 C46 57 36 57 34 53 M40 31 V35 M40 56 V60" stroke-linecap="round"/></svg>
    <h3>Best price</h3>
  </div>
  <div class="feature">
    <svg viewBox="0 0 80 80" fill="none" stroke="#3176b5" stroke-width="3"><circle cx="40" cy="28" r="10"/><path d="M22 62 C22 46 58 46 58 62 Z"/><circle cx="18" cy="32" r="8"/><path d="M4 60 C4 48 22 46 26 50"/><circle cx="62" cy="32" r="8"/><path d="M76 60 C76 48 58 46 54 50"/></svg>
    <h3>Professional team</h3>
  </div>
  <div class="feature">
    <svg viewBox="0 0 80 80" fill="none" stroke="#3176b5" stroke-width="3" stroke-linejoin="round"><rect x="12" y="36" width="12" height="32"/><path d="M24 40 L36 26 L38 10 C44 10 48 16 46 28 H64 C68 28 70 32 68 36 C70 40 68 44 66 46 C68 50 66 54 63 55 C64 60 62 64 58 64 H24"/></svg>
    <h3>High quality</h3>
  </div>
</section>

<section class="service" style="top:1252px">
  <div class="service-photo" role="img" aria-label="Photo of a bright white living room interior" style="background:linear-gradient(135deg,#f4f4f2,#d8dcdd 60%,#c9b88a)"></div>
  <div class="service-text">
    <h2>Interior design</h2>
    <p>If you are looking for renovation professionals who can bring out the best of your home or commercial space in Calgary, your search ends here. Our team is adept at blending layout, light, finishes and colour to suit the style you want. We take fine details of your preferences into account and design rooms of lasting quality that will serve you for years.</p>
    <a class="btn">See gallery</a>
  </div>
</section>

<section class="service flip" style="top:1614px">
  <div class="service-photo" role="img" aria-label="Photo of chrome taps over a stone counter" style="background:linear-gradient(135deg,#9a8d7c,#d7d3cc 50%,#6b5f52)"></div>
  <div class="service-text">
    <h2>Plumbing and heating</h2>
    <p>The true test of a good home is how well its water and heat run day after day. Our licensed team installs and repairs piping, fixtures, boilers and furnaces, and you can be sure of the best quality parts and sound work in your home or business. We never compromise on quality and comfort.</p>
    <a class="btn">See gallery</a>
  </div>
</section>

<section class="service" style="top:1976px">
  <div class="service-photo" role="img" aria-label="Photo of a ladder and paint cans beside colour swatches on a white wall" style="background:linear-gradient(90deg,#e66a4f,#f2b06c 25%,#f4e3a8 45%,#cfe3ec 65%,#4c86c6 85%,#f1f1f1)"></div>
  <div class="service-text">
    <h2>Painting</h2>
    <p>The importance of careful and tasteful painting on the feel of a room cannot be stressed enough. We offer our clients high quality interior and exterior painting. We start with the preparation of the walls and ceiling and give you a full range of finishes in every colour you like. Needless to say, our paints are of top quality.</p>
    <a class="btn">See gallery</a>
  </div>
</section>

<section class="service flip" style="top:2338px">
  <div class="service-photo" role="img" aria-label="Photo of a lounge chair on a light wooden floor" style="background:linear-gradient(180deg,#efe9e0,#d9c6a4 60%,#c8a878)"></div>
  <div class="service-text">
    <h2>Carpentry and flooring</h2>
    <p>Every Sort of Trade prides itself on skilled craftsmen who complete your carpentry and flooring work to perfection. Our team handles doors, windows, cabinets, trim, hardwood, tile and laminate floors. Your preferences and convenience are of the utmost importance to us, and you can count on us for work of the finest quality.</p>
    <a class="btn">See gallery</a>
  </div>
</section>

<section class="service" style="top:2700px">
  <div class="service-photo" role="img" aria-label="Photo of a curved white ceiling with recessed lights" style="background:linear-gradient(160deg,#7fa9c9,#e6ecef 45%,#b9c1c6)"></div>
  <div class="service-text">
    <h2>Electrical fitting &amp; fixtures</h2>
    <p>Good wiring and lighting shape how every space works and feels. Our journeyman electricians take on small or large projects, from panel upgrades and repairs to fixtures that suit each room, while making sure the quality and safety of every installation is uncompromised.</p>
    <a class="btn">See gallery</a>
  </div>
</section>

<section class="service flip" style="top:3062px">
  <div class="service-photo" role="img" aria-label="Photo of a welder working on a steel frame" style="background:linear-gradient(180deg,#8f8573,#b8ad98 50%,#d9d6cf)"></div>
  <div class="service-text">
    <h2>Welding &amp; fabrication</h2>
    <p>Steel and metal work is an essential part of many commercial and residential builds. We fabricate, repair and erect metal buildings, frames and parts that stand up to Alberta weather. Our team puts every effort into clean welds and strong joints that are practical, durable and of the finest quality.</p>
    <a class="btn">See gallery</a>
  </div>
</section>

<section class="more">
  <div class="more-line"></div>
  <a class="btn-outline">See more services</a>
</section>

<footer class="site-footer">
  <div class="message">
    <div class="footer-title">Send us message</div>
    <div class="fields">
      <div class="field">Enter your name</div>
      <div class="field">Enter your e-mail</div>
      <div class="field">Enter your phone</div>
    </div>
    <div class="field area">Enter your message</div>
    <div class="btn-subscribe">Subscribe</div>
  </div>
  <div class="contact">
    <div class="footer-title">Contact Us</div>
    Address<br>Calgary, Alberta<br>ph: (xxx) xxx xxx<br>e-mail: info@everysortoftrade.ca
  </div>
  <div class="follow">
    <div class="footer-title">Follow Us</div>
    <div class="social"><span></span><span></span><span></span></div>
  </div>
</footer>

</body>
</html>
```